Design our branded business card!

We'd love for you to design our business card and come up with a fitting design that reflects the Pivex brand. We're a growing tech startup with big ambitions. We've included our brand guidelines (contain colour palette), logo (EPS vector in CMYK) and old designs to help you on your way.

We'd like to keep the design fairly simple:

* Name
* Phone number
* Email address
* Website (www.pivex.life)
* Twitter (@pivex)
* Address (18 Wexham Row, Leeds, UK, LS9 4ZQ).

This would need to include print and cutting marks.

If you have any questions just let us know!

Target Market(s)

Businesses, Press and our customers!

Industry/Entity Type

Business

Contact Information for Business Card

* Name
* Phone number
* Email address
* Twitter (@pivex)

Font styles to use
Sans Serif

Requirements
Must have
• 1. Must have the Pivex logo included.
• 2. Must use the font 'Brandon Text' in either 'light' or 'thin' (https://www.typevault-demo.com/fonts/qrsfonts/halden-sans/)
• 3. Must use exact colours references from the brand guidelines. Colours outside of the brand guidelines will be discounted. White (transparent) backgrounds are fine.
• 4. Must contain the following information:
• * Name
• * Phone number
• * Email address
• * Website (www.pivex.life)
• * Twitter (@pivex)
• * Address (18 Wexham Row, Leeds, UK, LS9 4ZQ).
Nice to have
• Must use the font 'Brandon Text' in either 'light' or 'thin' (https://www.typevault-demo.com/fonts/qrsfonts/halden-sans/)
Should not have
• Colours outside of the brand guidelines will be discounted. White (transparent) backgrounds are fine.
• Avoid creating icons or including photography.

```html
<!DOCTYPE html>
<html lang="en">
<head>
<meta charset="utf-8">
<title>Pivex business card</title>
<link rel="stylesheet" href="https://fonts.googleapis.com/css2?family=Lato:wght@300;400&display=swap">
<style>
  :root {
    --backdrop: #505050;
    --brand-green: #80c475;
    --paper: #ffffff;
    --ink: #2f3a3a;
    --detail: #5f9a8a;
  }
  html, body {
    margin: 0;
    padding: 0;
    width: 1066px;
    height: 1200px;
    overflow: hidden;
    background: var(--backdrop);
    font-family: "Lato", sans-serif;
  }
  .card {
    position: absolute;
    left: 66px;
    width: 934px;
    height: 533px;
    overflow: hidden;
  }
  .card--front {
    top: 42px;
    background: var(--brand-green);
  }
  .card--back {
    top: 624px;
    background: var(--paper);
  }
  .brand {
    position: absolute;
    left: 222px;
    top: 202px;
    display: flex;
    align-items: center;
    gap: 26px;
    color: var(--paper);
  }
  .brand__dot {
    width: 128px;
    height: 128px;
    border-radius: 50%;
    background: var(--paper);
  }
  .brand__name {
    font-weight: 300;
    font-size: 100px;
    line-height: 1;
    letter-spacing: 1px;
    margin-top: -8px;
  }
  .back-shape {
    position: absolute;
    inset: 0;
  }
  .contact {
    position: absolute;
    left: 36px;
    top: 242px;
  }
  .contact__name {
    margin: 0 0 2px;
    font-weight: 400;
    font-size: 41px;
    line-height: 46px;
    color: var(--ink);
    letter-spacing: 0.5px;
  }
  .contact__list {
    list-style: none;
    margin: 0;
    padding: 0;
    font-weight: 400;
    font-size: 25px;
    line-height: 30.5px;
    color: var(--detail);
  }
  .contact__address { padding-left: 4px; }
</style>
</head>
<body>
  <section class="card card--front">
    <div class="brand">
      <span class="brand__dot"></span>
      <span class="brand__name">pivex</span>
    </div>
  </section>

  <section class="card card--back">
    <svg class="back-shape" width="934" height="533" viewBox="0 0 934 533" role="img" aria-label="Large brand-green curved shape in the brand colour">
      <circle cx="918" cy="200" r="532" fill="var(--brand-green)"/>
    </svg>
    <div class="contact">
      <h1 class="contact__name">MILES CARDEN JR.</h1>
      <ul class="contact__list">
        <li>+440(0) 7214 906</li>
        <li>mcardenjr@pivex.life</li>
        <li>www.pivex.life</li>
        <li>@pivex</li>
        <li class="contact__address">18 Wexham Row, Leeds, UK, LS9 4ZQ</li>
      </ul>
    </div>
  </section>
</body>
</html>
```